GLNSTC - Website Design

We require a WordPress website for an accounting firm.
Please review our concept design found on our development site:
http://mossyquarry.ca/glnstuw.
The client would like to carry the look and feel of the National Corporate site http://www.gln.ca as well.
The site must be mobile ready (responsive)
The client will be providing a collection of staff photos for a contact page
Accounting

```html
<!DOCTYPE html>
<html lang="en">
<head>
<meta charset="utf-8">
<title>GLN Marlow Finch &amp; Associates</title>
<link rel="stylesheet" href="https://fonts.googleapis.com/css2?family=Open+Sans:wght@400;600;700&display=swap">
<style>
:root{
  --olive:#8a8b47;
  --olive-dark:#7d7e3e;
  --ink:#2b2b2b;
  --body:#3a3a3a;
  --panel:#4a4a4a;
  --white:#ffffff;
  --footer:#d9dce2;
  --footer-ink:#3b3e44;
}
*{box-sizing:border-box;margin:0;padding:0}
html,body{width:946px;height:1200px;overflow:hidden}
body{position:relative;font-family:"Open Sans",Arial,sans-serif;background:var(--white);color:var(--body)}
.site-header{position:absolute;left:0;top:0;width:946px;height:95px;background:var(--white)}
.brand{position:absolute;left:78px;top:27px;display:flex;align-items:center;gap:9px}
.brand-square{width:28px;height:28px;background:var(--olive)}
.brand-name{font-size:17px;font-weight:600;color:var(--ink);letter-spacing:.3px;line-height:1.1}
.brand-tagline{display:block;font-size:10px;font-weight:400;letter-spacing:.4px;border-bottom:2px solid var(--olive);padding-bottom:2px;margin-top:2px}
.main-nav{position:absolute;top:36px;left:485px;display:flex;align-items:center}
.main-nav a{font-size:10.5px;font-weight:600;color:var(--ink);text-decoration:none;line-height:26px;margin-right:30px}
.main-nav a.active{background:var(--olive);color:var(--white);padding:0 10px;margin-right:29px}
.scenery{position:absolute;left:0;top:95px;width:946px;height:990px;
  background:
   linear-gradient(180deg,#3a3b3d 0%,#8a5a3a 7%,#e0833c 13%,#f0a250 17%,#7a5a4c 24%,#3e4048 30%,#5b4b3a 36%,#8a5a2c 42%,#a2441e 50%,#7a3a22 62%,#5c4a3a 75%,#766c68 85%,#b0aaa6 100%)}
.hero-title{position:absolute;left:79px;top:242px;font-size:17.5px;font-weight:600;letter-spacing:3.2px;line-height:32px;color:var(--white);text-transform:uppercase}
.slider-dots{position:absolute;left:444px;top:397px;display:flex;gap:4px}
.slider-dots span{width:10px;height:10px;border-radius:50%;background:var(--white)}
.slider-dots span.current{background:transparent;border:2px solid var(--white)}
.content-card{position:absolute;left:79px;top:435px;width:788px;height:650px;background:var(--white)}
.welcome{position:absolute;left:25px;top:24px;width:480px;font-size:19px;font-weight:600;line-height:26px;color:var(--olive)}
.intro{position:absolute;left:25px;top:88px;width:478px;font-size:11.2px;line-height:22.6px;color:var(--body)}
.feature-photo{position:absolute;left:28px;top:289px;width:465px;height:149px;background:linear-gradient(135deg,#c6ccd2 0%,#eef0f2 45%,#b9c2cc 75%,#6b7f98 100%)}
.closing{position:absolute;left:28px;top:463px;width:470px;font-size:11.2px;line-height:22.6px}
.read-more{position:absolute;left:31px;top:551px;width:79px;height:27px;background:var(--olive);color:var(--white);font-size:10.5px;font-weight:700;line-height:27px;text-align:center;text-decoration:none}
.services-panel{position:absolute;left:611px;top:447px;width:244px;height:623px;background:var(--panel);color:var(--white)}
.panel-head{position:absolute;left:18px;top:18px;font-size:11px;font-weight:700;letter-spacing:.2px}
.panel-arrows{position:absolute;right:20px;top:19px}
.service{position:absolute;left:18px;width:210px}
.service-photo{width:210px;height:82px}
.service h3{font-size:12px;font-weight:700;margin-top:16px;letter-spacing:.2px}
.service p{font-size:10.3px;line-height:16.2px;margin-top:6px;color:#ececec}
.site-footer{position:absolute;left:0;top:1085px;width:946px;height:115px;background:linear-gradient(180deg,#cfd3da,#dde0e5);border-top:1px solid #b6b9bf}
.connect{position:absolute;left:78px;top:30px;font-size:10.5px;font-weight:600;color:var(--footer-ink)}
.social{position:absolute;left:80px;top:60px;display:flex;gap:13px}
.social span{width:12px;height:12px;border-radius:50%;background:var(--footer-ink)}
.footer-nav{position:absolute;right:80px;top:29px;font-size:10.5px;font-weight:600;color:var(--footer-ink);word-spacing:1px}
.footer-nav a{color:inherit;text-decoration:none}
.footer-nav .sep{margin:0 7px}
.copyright{position:absolute;right:80px;top:56px;font-size:9.8px;font-weight:600;color:var(--footer-ink)}
</style>
</head>
<body>
<header class="site-header">
  <div class="brand">
    <div class="brand-square"></div>
    <div class="brand-name">MARLOW FINCH &amp; ASSOCIATES<span class="brand-tagline">CHARTERED PROFESSIONAL ACCOUNTANTS</span></div>
  </div>
  <nav class="main-nav">
    <a class="active" href="#">HOME</a><a href="#">PROFILE</a><a href="#">SERVICES</a><a href="#">RESOURCES</a><a href="#">CONTACT</a>
  </nav>
</header>

<div class="scenery" role="img" aria-label="Autumn mountain forest under an orange sunset sky"></div>
<h1 class="hero-title">Here are some interesting links<br>for you! Enjoy your stay</h1>
<div class="slider-dots"><span></span><span class="current"></span><span></span><span></span></div>

<main class="content-card">
  <h2 class="welcome">Welcome and thank you for visiting the GLN Marlow Finch &amp; Associates Website.</h2>
  <p class="intro">In addition to providing you with a profile of our firm and the services we provide, this Website has been designed to become a helpful resource tool to you, our valued clients and visitors. Our dedication to superior client service has brought us to the Internet as we endeavor to continue to provide the highest quality professional service and guidance. As you browse through our Website, you will see that we have not only highlighted background information on our firm and the services we provide, but have also included useful resources such as informative articles (in our Newsletter section) and interactive financial calculators (in our Financial Tools section).</p>
  <div class="feature-photo" role="img" aria-label="Hands reviewing a printed bar chart with a pen"></div>
  <p class="closing">While browsing through our Website, please feel free to contact us with any questions or comments you may have – we’d love to hear from you. We pride ourselves on being proactive and responsive to our clients’ inquiries and suggestions.</p>
  <a class="read-more" href="#">READ MORE</a>
</main>

<aside class="services-panel">
  <div class="panel-head">OUR SERVICES</div>
  <svg class="panel-arrows" width="30" height="14" viewBox="0 0 30 14" aria-hidden="true">
    <path d="M8 2 L3 7 L8 12" fill="none" stroke="#fff" stroke-width="2.4"/>
    <path d="M22 2 L27 7 L22 12" fill="none" stroke="#fff" stroke-width="2.4"/>
  </svg>
  <div class="service" style="top:49px">
    <div class="service-photo" role="img" aria-label="Laptop screen showing an accounting page" style="background:linear-gradient(135deg,#8a7a68,#3aa06a 50%,#c8c8c8)"></div>
    <h3>ACCOUNTING SERVICES</h3>
    <p>Providing financial information to our clients in a timely and accurate manner is a commitment that we feel .</p>
  </div>
  <div class="service" style="top:240px">
    <div class="service-photo" role="img" aria-label="Hand holding a printed financial chart" style="background:linear-gradient(90deg,#3c4048,#c9b8a8 40%,#eef0f4 60%,#d8dce6)"></div>
    <h3>FINANCIAL STATEMENTS</h3>
    <p>We can assist you in the preparation of your financial statements in accordance with&nbsp; professional standards.</p>
  </div>
  <div class="service" style="top:433px">
    <div class="service-photo" role="img" aria-label="Wooden tax letter blocks on a calculator" style="background:linear-gradient(180deg,#c8ccd0,#b89a70 45%,#3a3a3a 80%,#e8e8e8)"></div>
    <h3>TAX SERVICES</h3>
    <p>Providing financial information to our clients in a timely and accurate manner is a commitment that we feel .</p>
  </div>
</aside>

<footer class="site-footer">
  <div class="connect">CONNECT WITH US</div>
  <div class="social"><span></span><span></span><span></span><span></span></div>
  <nav class="footer-nav"><a href="#">HOME</a><span class="sep">|</span><a href="#">PROFILE</a><span class="sep">|</span><a href="#">CLIENT SERVICES</a><span class="sep">|</span><a href="#">RESOURCES</a><span class="sep">|</span><a href="#">CONTACT</a></nav>
  <div class="copyright">COPYRIGHTS @ 2015 ALL RIGHTS RESREVED</div>
</footer>
</body>
</html>
```